Darrow Consulting needs a quality & professional business card!

I am a recruitment and employment consultant from Brisbane, Australia and I had a fantastic logo organised by this community to I am hoping the business card will be the same.

I have attached the Darrow consulting logo that ideally would feature on the back of the business card. There are a number of logos for you to use as you see fit. I would like the colour cheme to match that of the Darrow Consulting logo. I also have a secondary company called Career Lantern Australia and I have included that logo as well. While it is an important part of the business I don't want this logo feature too predominantly as I am moving out of this space. This logo was created by myself and is of low quality. Feel free to use the icon and words however you want. The winning design will be smart, professional and eye-catching.

The information I am looking for in the business card is:
Name: Gavin Darrow
Position: Founder & Director
Phone: (07) 3519 6482
Mobile: 0431 586 207
Email: gavin@careerlantern.com.au

Target Market(s)

Recruiters, government, large companies

Contact Information for Business Card

Name: Gavin Darrow
Phone: (07) 3519 6482
Mobile: 0431 586 207
Web: www.careerlantern.com.au

Font styles to use
Serif
Sans Serif

Requirements
Must have
• Darrow Consulting Logo on reverse side
• Contact details on front side with smaller reference to Darrow Consulting logo and Career Lantern Australia logo

```html
<!DOCTYPE html>
<html lang="en">
<head>
<meta charset="utf-8">
<title>Darrow Consulting – Business Card</title>
<link rel="stylesheet" href="https://fonts.googleapis.com/css2?family=Oswald:wght@300;500;600&display=swap">
<style>
  :root {
    --page: #d6d7d8;
    --card: #202325;
    --orange: #e08a36;
    --blue: #2192cb;
    --green: #166f47;
    --ink: #ffffff;
    --muted: #c9ccce;
  }
  html, body {
    margin: 0;
    width: 1200px;
    height: 1200px;
    overflow: hidden;
    background: var(--page);
  }
  .sheet {
    width: 1200px;
    height: 1200px;
    display: flex;
    flex-direction: column;
    align-items: center;
    justify-content: center;
    gap: 80px;
  }
  .card {
    position: relative;
    width: 780px;
    height: 521px;
    overflow: hidden;
    background: var(--card);
    box-shadow: 0 6px 18px rgba(0,0,0,0.25);
    font-family: 'Oswald', sans-serif;
  }
  .card-art {
    position: absolute;
    inset: 0;
    background: linear-gradient(135deg,
      var(--orange) 0%,
      var(--blue) 24%,
      var(--green) 44%,
      var(--card) 64%);
    opacity: 0.9;
  }
  .holder {
    position: absolute;
    left: 101px;
    top: 250px;
    color: var(--ink);
    line-height: 1;
  }
  .holder-name {
    margin: 0;
    font-weight: 300;
    font-size: 35px;
    letter-spacing: -0.3px;
  }
  .holder-role {
    margin: 4px 0 0;
    font-weight: 600;
    font-size: 18px;
  }
  .contact-list {
    position: absolute;
    left: 476px;
    top: 217px;
    margin: 0;
    padding: 0;
    list-style: none;
  }
  .contact {
    display: flex;
    align-items: center;
    height: 25px;
    margin-bottom: 33px;
    color: var(--ink);
    font-weight: 300;
    font-size: 14px;
  }
  .contact-icon {
    width: 25px;
    height: 25px;
    margin-right: 21px;
    flex: none;
  }
  .icon-tile { fill: var(--ink); }
  .icon-glyph { fill: var(--card); }
  .icon-line { fill: none; stroke: var(--card); stroke-width: 1.2; }
  .brand {
    position: absolute;
    left: 482px;
    top: 246px;
    display: flex;
    align-items: center;
    gap: 10px;
  }
  .brand-mark {
    width: 20px;
    height: 20px;
    background: var(--blue);
  }
  .brand-name {
    font-weight: 500;
    font-size: 20px;
    color: var(--muted);
    letter-spacing: 1px;
    line-height: 1;
  }
</style>
</head>
<body>
<main class="sheet">

  <section class="card card-front">
    <div class="card-art" role="img" aria-label="Decorative diagonal shapes in orange, blue and green"></div>
    <div class="holder">
      <p class="holder-name">GAVIN DARROW</p>
      <p class="holder-role">FOUNDER &amp; DIRECTOR</p>
    </div>
    <ul class="contact-list">
      <li class="contact contact-office">
        <svg class="contact-icon" viewBox="0 0 15 15" aria-hidden="true">
          <rect class="icon-tile" width="15" height="15" rx="3"/>
          <path class="icon-glyph" d="M7.5 2.5a3.4 3.4 0 0 0-3.4 3.4c0 2.4 3.4 6.4 3.4 6.4s3.4-4 3.4-6.4a3.4 3.4 0 0 0-3.4-3.4zm0 4.8a1.4 1.4 0 1 1 0-2.8 1.4 1.4 0 0 1 0 2.8z"/>
        </svg>
        (07) 3519 6482
      </li>
      <li class="contact contact-mobile">
        <svg class="contact-icon" viewBox="0 0 15 15" aria-hidden="true">
          <rect class="icon-tile" width="15" height="15" rx="3"/>
          <path class="icon-glyph" d="M5 3h1.8l.9 2.4-1.1.8c.5 1.2 1.3 2 2.4 2.5l.8-1.1 2.4.9V10.3c0 .6-.5 1-1.1 1C6.6 11 4 8.4 3.8 4.1 3.8 3.5 4.3 3 5 3z"/>
        </svg>
        0431 586 207
      </li>
      <li class="contact contact-email">
        <svg class="contact-icon" viewBox="0 0 15 15" aria-hidden="true">
          <rect class="icon-tile" width="15" height="15" rx="3"/>
          <rect class="icon-line" x="3" y="4.5" width="9" height="6.5"/>
          <polyline class="icon-line" points="3,4.5 7.5,8.3 12,4.5"/>
        </svg>
        GAVIN@CAREERLANTERN.COM.AU
      </li>
    </ul>
  </section>

  <section class="card card-back">
    <div class="card-art" role="img" aria-label="Decorative diagonal shapes in orange, blue and green"></div>
    <div class="brand">
      <span class="brand-mark"></span>
      <span class="brand-name">DARROW CONSULTING</span>
    </div>
  </section>

</main>
</body>
</html>
```